Bref créative
brochure and folder for a4 brochures
Brush Wave
Protecting your assets
Need a brochure template to use for Strata painting and residential painting
"STRATA BROCHURE COPY"
Brush Wave, the easy choice for strata paint works
Why strata managers love Brush Wave
Work with a company that focuses on your needs – a company that can get your strata painting works done with no hassle. We’ve been in business for over 20 years; we’re your one-stop shop for painting and remedial maintenance, and we get it right the first time.
At Brush Wave, we understand you need:
• Quality painting, project managed by us so you don’t have to take endless phone calls
• Great-value price: We take time to make sure of this
• Great ideas for colour schemes (saving the owners up to $700)
• Remedial repairs overseen by a qualified master builder
Why choose Brush Wave?
The Brush Wave difference means we turn up when we’re supposed to and finish on schedule. All our tradespeople are friendly, professional – and we promise that your site will be cleaner when we’ve finished than when we started.
Once you’ve accepted our quote, we can start within 24 hours and we manage the job from start to finish. You’ll be a hero with owners and you have peace of mind knowing the job’s under control.
Life’s easier with Brush Wave
Take the headache out of your strata painting works. Call Brush Wave on 1300 482 915.
What clients say about us
“Derek and his team have skilfully and professionally painted our property comprising 17 apartments and townhouses. The progress of the work has been clean and efficient and the result is excellent.”
Owen Falkirk, Moorings, Henley
“Communication is the key to successfully managing a project and Derek and his team exceeded expectations with updates concerning all aspects of the work.“ Neil Barker, Randwick
Add value to your new home before you move in, with Brush Wave
"RESIDENTIAL BROCHURE"
Start your new life with a clean freshly painted house
We’ve been in business for over 20 years and we know that when you move into your new home, it’s best to do all the basics first – quickly, with no fuss.
At Brush Wave, we understand you want:
• Quick, clean work: We can start within 24 hours and be in and out before you know it
• Good value: We also make remedial repairs so you get a perfect finish
• Great ideas for colour schemes (saving you up to $700)
• Friendly professional tradies you’ll be happy to have around your home
We turn up when we’re supposed to and finish on time. We’ll quote as soon as you pick up the keys and can advise on colours that will create just the right atmosphere. What’s more, your new home will be cleaner than when we started.
We guarantee
• Great-value price: We’ll help you make sure of this
• Impressive service: Fast, clean, quality job, and responsive to your needs
For feel-good factor, there’s nothing like a fresh splash of colour
If you’d like to start fresh, call Brush Wave on 1300 482 915.
"When dealing with Brush Wave we were given expert and professional advice in choosing colours for our beach house... The end result was great." Fiona Darrowby
Real Estate
corporate FOR STRATA
professional FOR RESIDENTIAL
need one brochure for residential painting and one for strata painting and a folder that we can use for both brochures
please use logo only do not use NSW or website under logo
please see attachment
please only use brushwave not background, lines or website under logo
another log for your use

```html
<!DOCTYPE html>
<html lang="en">
<head>
<meta charset="utf-8">
<title>Brush Wave – Strata and Residential Brochures with Folder</title>
<link href="https://fonts.googleapis.com/css2?family=Oswald:wght@500;700&family=Open+Sans:wght@400;700&display=swap" rel="stylesheet">
<style>
  :root{
    --board-dark:#2b2b2d;
    --board-mid:#4a4a4d;
    --bar:#1c1c1e;
    --label:#f2f2f2;
    --paper:#ffffff;
    --pocket-blue:#bfe3ee;
    --brand-blue:#1f4e8c;
    --brand-red:#d2232a;
    --accent-yellow:#ffd21f;
    --accent-orange:#f39a1e;
    --sky-top:#3e7fc4;
    --sky-low:#9cc9e6;
    --text-grey:#555a60;
    --line-grey:#c9cdd2;
  }
  *{box-sizing:border-box;margin:0;padding:0}
  html,body{width:1200px;height:602px;overflow:hidden}
  body{
    font-family:"Open Sans",Arial,sans-serif;
    background:radial-gradient(ellipse at 50% 45%,var(--board-mid) 0%,var(--board-dark) 75%);
    position:relative;
  }
  .title-bar{
    position:absolute;left:0;top:0;width:1200px;height:30px;
    background:var(--bar);display:flex;align-items:center;gap:14px;padding-left:318px;
  }
  .title-bar .brand{color:var(--label);font-weight:700;font-size:12px;display:flex;align-items:center;gap:5px}
  .dot{display:inline-block;width:1em;height:1em;border-radius:50%;background:var(--accent-yellow);flex:none}
  .title-bar p{color:var(--label);font-size:10px;font-family:Georgia,"Times New Roman",serif}
  .label{position:absolute;color:var(--label);font-family:Georgia,"Times New Roman",serif;font-weight:700;font-size:14px}

  /* Folder outside */
  .folder-outside{position:absolute;left:100px;top:108px;width:240px;height:252px;display:flex;box-shadow:0 4px 10px rgba(0,0,0,.5)}
  .folder-outside .back{width:50%;background:var(--paper);position:relative}
  .folder-outside .front{width:50%;background:var(--pocket-blue)}
  .logo{display:flex;align-items:center;gap:.3em;color:var(--brand-blue);font-weight:700;font-family:"Open Sans",Arial,sans-serif;white-space:nowrap}
  .folder-outside .logo{position:absolute;left:12px;top:48px;font-size:11px}
  .folder-outside .contact{position:absolute;left:12px;bottom:18px;font-size:5px;line-height:1.5;color:var(--text-grey)}

  /* Folder inside */
  .folder-inside{position:absolute;left:103px;top:385px;width:297px;height:212px;background:var(--paper);box-shadow:0 4px 10px rgba(0,0,0,.5);overflow:hidden}
  .folder-inside .logo{position:absolute;left:12px;top:10px;font-size:8px}
  .folder-inside h2{position:absolute;left:34px;top:38px;width:160px;font-family:Oswald,Impact,sans-serif;font-weight:700;font-size:18px;line-height:1.05;color:var(--brand-blue)}
  .folder-inside .sub{position:absolute;left:34px;top:82px;width:160px;font-size:5.5px;font-weight:700;color:var(--brand-red);text-transform:uppercase}
  .folder-inside .pour{position:absolute;right:0;top:18px;width:88px;height:98px;background:linear-gradient(160deg,var(--accent-orange),#8a3b12 55%,var(--accent-yellow));border-radius:40% 0 0 30%}
  .pocket{position:absolute;top:122px;height:90px;width:146px;background:var(--pocket-blue);display:flex;align-items:center;justify-content:center;text-align:center;font-size:6px;line-height:1.4;color:var(--brand-blue)}
  .pocket.left{left:0;border-top-right-radius:18px}
  .pocket.right{right:0;border-top-left-radius:18px}

  /* Brochure page, sized with em */
  .brochure{position:absolute;width:37.5em;height:53em;background:var(--paper);overflow:hidden;box-shadow:0 4px 10px rgba(0,0,0,.5)}
  .brochure .hero{position:absolute;left:0;top:0;width:100%;height:19em;background:linear-gradient(180deg,var(--sky-top),var(--sky-low) 60%,#c8c4b8)}
  .brochure .headline{position:absolute;left:1.5em;right:1.5em;top:1.5em}
  .brochure h2{font-family:Oswald,Impact,sans-serif;font-weight:700;font-size:2.6em;line-height:1;color:var(--accent-yellow);max-width:8em;text-shadow:0 .05em .1em rgba(0,0,0,.35)}
  .brochure .tagline{margin-top:.5em;font-size:.9em;font-weight:700;color:var(--paper);max-width:22em}
  .brochure .splash{position:absolute;left:0;top:16em;width:100%;height:12em;background:linear-gradient(100deg,var(--brand-red) 0%,var(--accent-orange) 35%,var(--accent-yellow) 70%);clip-path:polygon(0 20%,100% 0,100% 85%,0 100%)}
  .brochure .content{position:absolute;left:2em;right:2em;top:29em;bottom:5em;display:flex;flex-direction:column;gap:1em;overflow:hidden}
  .brochure .lead{font-size:1.15em;font-weight:700;color:var(--brand-blue);line-height:1.2}
  .brochure .cols{flex:1;display:flex;gap:1.5em;min-height:0}
  .brochure .col{flex:1;font-size:.72em;line-height:1.35;color:var(--text-grey);overflow:hidden}
  .brochure .col b{color:var(--brand-blue);display:block;margin-bottom:.2em}
  .brochure .thumb{height:9em;background:linear-gradient(135deg,#d9c9a8,#8fa8b8);margin-bottom:.6em}
  .brochure footer{position:absolute;left:0;bottom:0;width:100%;height:4em;background:var(--accent-yellow);display:flex;align-items:center;justify-content:space-between;padding:0 2em}
  .brochure footer .logo{font-size:1.1em}
  .brochure footer .phone{font-family:Oswald,Impact,sans-serif;font-weight:700;font-size:1.3em;color:var(--brand-blue)}
  .residential .hero{background:linear-gradient(180deg,#6aa9d8,#d9e8f0 55%,#d6c2a0)}
  .residential .splash{background:linear-gradient(100deg,var(--accent-yellow),var(--accent-orange) 60%,var(--brand-red))}

  .strata-page{left:390px;top:103px;font-size:4px}
  .resident-page{left:455px;top:385px;font-size:3.2px}
  .fan-1{left:610px;top:150px;font-size:4.6px}
  .fan-2{left:800px;top:150px;font-size:4.6px}
  .fan-3{left:990px;top:150px;font-size:4.6px}
</style>
</head>
<body>
  <header class="title-bar">
    <span class="brand"><span class="dot"></span>Brush Wave</span>
    <p>Marketing Materials for Flyers Brochure and Folder for A4 Brochures | Brush Wave "Protecting Your Assets"</p>
  </header>

  <span class="label" style="left:135px;top:62px">Folder Outside</span>
  <section class="folder-outside">
    <div class="back">
      <div class="logo"><span class="dot"></span>Brush Wave</div>
      <p class="contact">Protecting your assets<br>Call 1300 482 915<br>Sydney NSW</p>
    </div>
    <div class="front"></div>
  </section>

  <span class="label" style="left:390px;top:62px">Strata Brochure Copy</span>
  <article class="brochure strata strata-page">
    <div class="hero" role="img" aria-label="Photo of a strata apartment block against a blue sky"></div>
    <div class="headline"><h2>SYDNEYS FAVOURITE PAINTING FIRM</h2><p class="tagline">The easy choice for strata paint works</p></div>
    <div class="splash" role="img" aria-label="Paint cans with yellow and orange paint splash"></div>
    <div class="content">
      <p class="lead">Brush Wave, the easy choice for strata paint works</p>
      <div class="cols">
        <div class="col"><b>Why strata managers love Brush Wave</b>Work with a company that focuses on your needs – a company that can get your strata painting works done with no hassle. We’ve been in business for over 20 years; we’re your one-stop shop for painting and remedial maintenance.</div>
        <div class="col"><div class="thumb" role="img" aria-label="Photo of a freshly painted townhouse"></div><b>Why choose Brush Wave?</b>We turn up when we’re supposed to and finish on schedule.</div>
      </div>
    </div>
    <footer><span class="logo"><span class="dot"></span>Brush Wave</span><span class="phone">1300 482 915</span></footer>
  </article>

  <span class="label" style="left:145px;top:364px">Folder Inside</span>
  <section class="folder-inside">
    <div class="logo"><span class="dot"></span>Brush Wave</div>
    <h2>SYDNEYS FAVOURITE PAINTING FIRM</h2>
    <p class="sub">20 years painting Sydney properties</p>
    <div class="pour" role="img" aria-label="Paint pouring from tipped paint cans"></div>
    <div class="pocket left">Protecting<br>your<br>assets</div>
    <div class="pocket right">Brush Wave<br>for every project</div>
  </section>

  <span class="label" style="left:455px;top:364px">Resident Brochure</span>
  <article class="brochure residential resident-page">
    <div class="hero" role="img" aria-label="Photo of a freshly painted family home"></div>
    <div class="headline"><h2>SYDNEYS FAVOURITE PAINTING FIRM</h2><p class="tagline">Start your new life with a clean freshly painted house</p></div>
    <div class="splash" role="img" aria-label="Paint cans with yellow and orange paint splash"></div>
    <div class="content">
      <p class="lead">Add value to your new home before you move in</p>
      <div class="cols">
        <div class="col"><b>At Brush Wave, we understand you want:</b>Quick, clean work: we can start within 24 hours and be in and out before you know it. Good value and great ideas for colour schemes.</div>
        <div class="col"><div class="thumb" role="img" aria-label="Photo of a painted living room"></div><b>We guarantee</b>Great-value price and impressive service.</div>
      </div>
    </div>
    <footer><span class="logo"><span class="dot"></span>Brush Wave</span><span class="phone">1300 482 915</span></footer>
  </article>

  <article class="brochure strata fan-1">
    <div class="hero" role="img" aria-label="Photo of a strata apartment block against a blue sky"></div>
    <div class="headline"><h2>SYDNEYS FAVOURITE PAINTING FIRM</h2><p class="tagline">The easy choice for strata paint works</p></div>
    <div class="splash" role="img" aria-label="Paint cans with yellow and orange paint splash"></div>
    <div class="content">
      <p class="lead">Life’s easier with Brush Wave</p>
      <div class="cols">
        <div class="col"><b>What clients say about us</b>“Derek and his team have skilfully and professionally painted our property comprising 17 apartments and townhouses.” Owen Falkirk, Moorings, Henley</div>
        <div class="col"><div class="thumb" role="img" aria-label="Photo of a painted apartment facade"></div>“Communication is the key to successfully managing a project.” Neil Barker, Randwick</div>
      </div>
    </div>
    <footer><span class="logo"><span class="dot"></span>Brush Wave</span><span class="phone">1300 482 915</span></footer>
  </article>

  <article class="brochure residential fan-2">
    <div class="hero" role="img" aria-label="Photo of a freshly painted family home"></div>
    <div class="headline"><h2>SYDNEYS FAVOURITE PAINTING FIRM</h2><p class="tagline">Start your new life with a clean freshly painted house</p></div>
    <div class="splash" role="img" aria-label="Paint cans with yellow and orange paint splash"></div>
    <div class="content">
      <p class="lead">For feel-good factor, there’s nothing like a fresh splash of colour</p>
      <div class="cols">
        <div class="col"><b>Start fresh</b>If you’d like to start fresh, call Brush Wave on 1300 482 915.</div>
        <div class="col"><div class="thumb" role="img" aria-label="Photo of a painted beach house"></div>“We were given expert and professional advice in choosing colours for our beach house.” Fiona Darrowby</div>
      </div>
    </div>
    <footer><span class="logo"><span class="dot"></span>Brush Wave</span><span class="phone">1300 482 915</span></footer>
  </article>

  <article class="brochure strata fan-3">
    <div class="hero" role="img" aria-label="Photo of a strata apartment block against a blue sky"></div>
    <div class="headline"><h2>SYDNEYS FAVOURITE PAINTING FIRM</h2><p class="tagline">The easy choice for strata paint works</p></div>
    <div class="splash" role="img" aria-label="Paint cans with yellow and orange paint splash"></div>
    <div class="content">
      <p class="lead">At Brush Wave, we understand you need:</p>
      <div class="cols">
        <div class="col"><b>Quality painting</b>Project managed by us so you don’t have to take endless phone calls. Remedial repairs overseen by a qualified master builder.</div>
        <div class="col"><div class="thumb" role="img" aria-label="Photo of a repainted strata complex"></div>Once you’ve accepted our quote, we can start within 24 hours.</div>
      </div>
    </div>
    <footer><span class="logo"><span class="dot"></span>Brush Wave</span><span class="phone">1300 482 915</span></footer>
  </article>
</body>
</html>
```